Gift Bag Design

We need a gift bag designed for our practice. We are a upscale optometry practice. The gift bags are given to our patients when they pick up their eyewear. We would like to see a gift bag designed with the use of dark grays and purples with a nice texture. We want simple, elegant, and upscale. We really like something with the texture of lamivo laminate ashen reed style number 4812-93. We also use pantone 2695U for our purple colors.
Target Market(s)
Middle aged women that are fashionable
Industry/Entity Type
Eyewear
Requirements
Must have
- We must have use of our logo, which we've attached. The name of the business must be "clear path" or "bright lens studio", whichever works better. The dimensions of the bag must be 20.5 cm high x 12.5 cm wide x 7.5 deep.
Nice to have
- Our phone number 555-217-6094 and our website www.BrightLensStudioXY.com
Should not have
- No red, yellow

```html
<!DOCTYPE html>
<html lang="en">
<head>
<meta charset="utf-8">
<title>Clear Path Gift Bag</title>
<link rel="stylesheet" href="https://fonts.googleapis.com/css2?family=Kaushan+Script&family=Marcellus&display=swap">
<style>
  :root {
    --bag-purple: #3d1a52;
    --pattern-tone: #6e5488;
    --ink-white: #ffffff;
    --gap-white: #ffffff;
  }
  * { margin: 0; padding: 0; box-sizing: border-box; }
  html, body { width: 1200px; height: 918px; overflow: hidden; background: var(--gap-white); }
  .canvas { position: relative; width: 1200px; height: 918px; }
  .bag-face {
    position: absolute; top: 0; height: 918px;
    background: var(--bag-purple); overflow: hidden;
  }
  .bag-face--front { left: 0; width: 560px; }
  .bag-face--side { left: 642px; width: 558px; }
  .pattern-art { position: absolute; inset: 0; }
  .script-title {
    position: absolute; left: 0; right: 0; text-align: center;
    font-family: "Kaushan Script", cursive; color: var(--ink-white);
    white-space: nowrap; line-height: 1;
  }
  .bag-face--front .script-title { top: 218px; font-size: 62px; }
  .bag-face--side .script-title { top: 44px; font-size: 74px; letter-spacing: 2px; }
  .brand-plate {
    position: absolute; left: 50%; top: 756px; transform: translateX(-50%);
    width: 156px; height: 77px; background: var(--ink-white);
    display: flex; align-items: center; justify-content: center; gap: 6px;
  }
  .brand-plate__dot { width: 10px; height: 10px; border-radius: 50%; background: var(--bag-purple); flex: none; }
  .brand-plate__name {
    font-family: "Marcellus", serif; font-size: 15px; color: var(--bag-purple);
    white-space: nowrap;
  }
  .contact {
    position: absolute; left: 0; right: 0; text-align: center;
    font-family: "Marcellus", serif; color: var(--ink-white); white-space: nowrap;
  }
  .contact--phone { top: 846px; font-size: 20px; }
  .contact--web { top: 876px; font-size: 18px; letter-spacing: 0.5px; }
</style>
</head>
<body>
<div class="canvas">
  <section class="bag-face bag-face--front">
    <svg class="pattern-art" width="560" height="918" viewBox="0 0 560 918" role="img" aria-label="Sweeping band of repeated eye motif pattern">
      <path d="M0,700 Q300,580 560,296 L560,560 Q300,650 0,752 Z" fill="var(--pattern-tone)" opacity="0.55"/>
    </svg>
    <h1 class="script-title">Clear Path</h1>
    <div class="brand-plate"><span class="brand-plate__dot"></span><span class="brand-plate__name">bright lens studio</span></div>
    <p class="contact contact--phone">P : 555-217-6094</p>
    <p class="contact contact--web">WWW.BRIGHTLENSSTUDIOXY.COM</p>
  </section>
  <section class="bag-face bag-face--side">
    <svg class="pattern-art" width="558" height="918" viewBox="642 0 558 918" role="img" aria-label="Five diamond clusters of repeated eye motif pattern">
      <g fill="var(--pattern-tone)" opacity="0.55">
        <path d="M784,120 L904,208 L784,296 L664,208 Z"/>
        <path d="M1056,120 L1176,208 L1056,296 L936,208 Z"/>
        <path d="M920,292 L1040,380 L920,468 L800,380 Z"/>
        <path d="M784,464 L904,552 L784,640 L664,552 Z"/>
        <path d="M1056,464 L1176,552 L1056,640 L936,552 Z"/>
      </g>
    </svg>
    <h2 class="script-title">clear path</h2>
    <div class="brand-plate"><span class="brand-plate__dot"></span><span class="brand-plate__name">bright lens studio</span></div>
    <p class="contact contact--phone">P : 555-217-6094</p>
    <p class="contact contact--web">WWW.BRIGHTLENSSTUDIOXY.COM</p>
  </section>
</div>
</body>
</html>
```